letterhead design

We have a business card with logo, ink etc and want to develop letterhead that uses the elements of the business card logo.
Must haves...and they should be designed in, not just plopped in :)
Dr. Lyle Varden
2817 W Marlow Street
Fresno, CA 93614
559-382-6157 p
559-382-7043 f
info@brindlespine.com
www.brindlespine.com
www.facebook.com/brindlespn
Updates

Rather than just have the logo on the page, is there someway to silkscreen it in the background to fill the page?

Reason: I was out of town for a week.

Industry/Entity Type

Business

Requirements
Nice to have
• I'd like the logo somehow silk screened in the background of the paper as well.

```html
<!DOCTYPE html>
<html lang="en">
<head>
<meta charset="utf-8">
<title>Brindle Spine Letterhead</title>
<link href="https://fonts.googleapis.com/css2?family=Arimo:wght@400&display=swap" rel="stylesheet">
<style>
  :root {
    --mat: #282828;
    --paper: #ffffff;
    --ink: #2b2b2b;
    --rule-dark: #3a3a3a;
    --rule-soft: #b5b5b5;
    --ghost: #ebebeb;
  }
  * { margin: 0; padding: 0; box-sizing: border-box; }
  html, body {
    width: 903px;
    height: 1200px;
    overflow: hidden;
    background: var(--mat);
    font-family: "Arimo", Arial, sans-serif;
    color: var(--ink);
  }
  .letterhead {
    position: absolute;
    left: 83px;
    top: 67px;
    width: 720px;
    height: 1019px;
    background: var(--paper);
  }
  .rule { position: absolute; height: 3px; }
  .rule--top {
    left: 229px; top: 8px; width: 491px;
    background: linear-gradient(to right, rgba(181,181,181,0), var(--rule-soft) 55%, #9a9a9a);
  }
  .rule--header {
    left: 229px; top: 87px; width: 491px;
    background: linear-gradient(to right, rgba(58,58,58,0), var(--rule-soft) 40%, var(--rule-dark) 80%);
  }
  .brand {
    position: absolute;
    right: 8px;
    top: 12px;
    width: 165px;
    height: 73px;
    display: flex;
    align-items: center;
    justify-content: center;
    font-size: 22px;
    white-space: nowrap;
    color: var(--ink);
  }
  .doctor {
    position: absolute;
    right: 171px;
    top: 72px;
    font-size: 15px;
    line-height: 1;
  }
  .backdrop-name {
    position: absolute;
    left: 182px;
    top: 430px;
    width: 355px;
    height: 160px;
    display: flex;
    align-items: center;
    justify-content: center;
    font-size: 50px;
    white-space: nowrap;
    color: var(--ghost);
  }
  .rule--footer {
    left: 0; top: 962px; width: 570px;
    background: linear-gradient(to right, #9a9a9a, var(--rule-soft) 60%, rgba(181,181,181,0));
  }
  .rule--base {
    left: 0; top: 1010px; width: 720px;
    background: linear-gradient(to right, var(--rule-dark), #7a7a7a 50%, rgba(160,160,160,0.3));
  }
  .address {
    position: absolute;
    left: 7px;
    top: 967px;
    font-size: 18px;
    line-height: 1;
    white-space: nowrap;
  }
  .contact {
    position: absolute;
    left: 10px;
    top: 987px;
    font-size: 11px;
    line-height: 12px;
    white-space: nowrap;
  }
  .contact .email { margin-left: 20px; }
  .web {
    position: absolute;
    right: 11px;
    top: 987px;
    font-size: 13.5px;
    line-height: 11.5px;
    text-align: right;
    white-space: nowrap;
  }
</style>
</head>
<body>
  <div class="letterhead">
    <div class="rule rule--top"></div>
    <div class="brand">Brindle Spine</div>
    <div class="doctor">Dr. Lyle Varden</div>
    <div class="rule rule--header"></div>

    <div class="backdrop-name" aria-hidden="true">Brindle Spine</div>

    <div class="rule rule--footer"></div>
    <div class="address">2817 W Marlow Street, Corvale, CA 93614</div>
    <div class="contact">
      <div>555-382-6157p</div>
      <div>555-382-7043f<span class="email">info@brindlespine.com</span></div>
    </div>
    <div class="web">
      <div>www.brindlespine.com</div>
      <div>www.friendwall.net/brindlespn</div>
    </div>
    <div class="rule rule--base"></div>
  </div>
</body>
</html>
```